Calm Harbor Blueprint

I need a on page electronic flyer for this coaching program. I want a silhouette to accompany the case the copy starts with. I have the copy written but need it put together in a striking way.

Target Market(s)

towards higher net worth individuals

Industry/Entity Type

Electronic

```html
<!DOCTYPE html>
<html lang="en">
<head>
<meta charset="utf-8">
<title>Calm Harbor Blueprint – Coaching Flyer</title>
<link rel="stylesheet" href="https://fonts.googleapis.com/css2?family=Comfortaa:wght@400;700&family=Arimo:wght@400;700&family=Tinos:wght@700&display=swap">
<style>
  :root {
    --orange: #f5a511;
    --orange-text: #f2a20c;
    --white: #ffffff;
    --sky: #d3e8fb;
    --blue: #2a93ee;
    --pink: #f8c2c3;
    --red: #e4131b;
    --ink: #141414;
  }
  html, body { margin: 0; padding: 0; overflow: hidden; }
  body { width: 848px; height: 1200px; background: var(--sky); }
  .flyer {
    position: relative; width: 848px; height: 1200px; overflow: hidden;
    font-family: "Arimo", Arial, sans-serif; color: var(--ink);
  }
  .backdrop { position: absolute; inset: 0; }

  .headline {
    position: absolute; left: 34px; top: 14px; margin: 0;
    font-family: "Comfortaa", sans-serif; font-weight: 400;
    font-size: 35px; line-height: 44px; color: var(--white); letter-spacing: -0.3px;
  }
  .headline strong { font-weight: 700; }

  .subhead {
    position: absolute; left: 36px; top: 124px; margin: 0;
    font-family: "Comfortaa", sans-serif; font-weight: 400;
    font-size: 31px; line-height: 42px; color: var(--orange-text);
    transform: rotate(-1.2deg); transform-origin: left top;
  }
  .subhead strong { font-weight: 700; }

  .silhouette {
    position: absolute; left: 90px; top: 228px; width: 222px; height: 228px;
    background: linear-gradient(180deg, #1c1c1c, #050505);
    border-radius: 90px 90px 10px 10px;
  }

  .case-story {
    position: absolute; left: 311px; top: 238px; width: 482px; height: 271px;
    box-sizing: border-box; padding: 16px 24px 0 26px; background: var(--pink);
    border: 2px solid var(--red); border-radius: 20px;
    font-size: 13.4px; font-weight: 700; line-height: 17px;
  }
  .case-story p { margin: 0 0 15px; }

  .case-tag {
    position: absolute; left: 82px; top: 440px; width: 228px; height: 64px;
    background: var(--red); border-radius: 26px; color: var(--white);
    font-family: "Tinos", serif; font-weight: 700; font-size: 25px; line-height: 26px;
    text-align: center; padding-top: 6px; box-sizing: border-box;
    transform: rotate(-8deg); box-shadow: 2px 3px 4px rgba(0,0,0,0.25);
  }

  .intro {
    position: absolute; left: 64px; top: 536px; width: 752px; margin: 0;
    font-size: 13.4px; line-height: 16.5px; font-weight: 700;
  }

  .body-copy {
    position: absolute; left: 64px; top: 622px; width: 420px;
    font-size: 13.4px; line-height: 17px;
  }
  .body-copy p { margin: 0 0 16px; }
  .body-copy .question { font-weight: 700; }
  .body-copy .list-intro { margin-bottom: 1px; }
  .benefits { list-style: none; margin: 0 0 16px; padding: 0; }
  .benefits li { position: relative; padding-left: 26px; }
  .benefits li::before {
    content: ""; position: absolute; left: 2px; top: 5px;
    width: 7px; height: 7px; background: var(--blue);
  }

  .coach-card {
    position: absolute; left: 519px; top: 608px; width: 329px; height: 288px;
    box-sizing: border-box; padding: 24px 26px 0 29px;
    background: var(--blue); border-radius: 28px 0 0 28px; color: var(--white);
    font-size: 15.4px; line-height: 19px;
  }
  .coach-card p { margin: 0 0 19px; }
  .coach-card strong { font-weight: 700; }

  .brand-mark {
    position: absolute; left: 588px; top: 970px; width: 180px; height: 180px;
    border-radius: 50%; background: var(--blue);
    display: flex; align-items: center; justify-content: center; text-align: center;
    font-family: "Arimo", sans-serif; font-weight: 700; font-size: 22px; line-height: 26px;
    color: var(--white);
  }

  .offer {
    position: absolute; left: 42px; top: 1044px; width: 452px; height: 143px;
    box-sizing: border-box; padding: 14px 22px;
    background: var(--blue); border-radius: 24px; color: var(--white);
  }
  .offer-title { margin: 0 0 6px; font-family: "Tinos", serif; font-weight: 700; font-size: 17px; }
  .offer-list { list-style: none; margin: 0 0 16px; padding: 0 0 0 14px;
    font-family: "Tinos", serif; font-weight: 700; font-size: 14px; line-height: 18px; }
  .offer-list li::before { content: "\25A0\00a0"; font-size: 10px; }
  .offer-contact { margin: 0; font-family: "Tinos", serif; font-weight: 700; font-size: 14.5px; }
  .price {
    position: absolute; left: 270px; top: 14px; width: 160px; text-align: center;
    font-family: "Tinos", serif; font-weight: 700; font-size: 19px; line-height: 20px;
  }
  .price .amount { display: block; font-size: 32px; line-height: 36px; }
</style>
</head>
<body>
<main class="flyer">
  <svg class="backdrop" width="848" height="1200" viewBox="0 0 848 1200" aria-hidden="true">
    <defs>
      <linearGradient id="skyFade" x1="0" y1="0" x2="0" y2="1">
        <stop offset="0" stop-color="#dcedfc"/>
        <stop offset="1" stop-color="#b8dbf8"/>
      </linearGradient>
    </defs>
    <rect width="848" height="1200" fill="url(#skyFade)"/>
    <path d="M0 0 H848 V585 C620 520 330 445 0 430 Z" fill="var(--orange)"/>
    <path d="M0 106 L848 92 L848 192 L0 224 Z" fill="var(--white)"/>
    <path d="M0 1112 C250 1090 500 1120 848 1070 V1200 H0 Z" fill="#aed6f7" opacity="0.6"/>
  </svg>

  <h1 class="headline">Sometimes the <strong>best financial</strong> advice<br><strong>isn’t about numbers…</strong></h1>
  <h2 class="subhead"><strong>Calm Harbor Blueprint:</strong><br>From Financial <strong>Worries</strong> to <strong>Wealth Satisfaction</strong></h2>

  <div class="silhouette" role="img" aria-label="Dark silhouette of a man’s head and shoulders"></div>

  <section class="case-story">
    <p>A 49 year old attorney, Steve was used to success and rising net worth. But with huge losses in the market crash, layoffs at his firm, his kids heading for college and the stagnant economy stretching ahead, his usual optimism is gone.</p>
    <p>With his anxiety growing, Steve doubts his own decision making ability. His confidence slipping, he stopped opening his financial statements and could barely speak to his financial advisor. He thought if his advisor said “hang in there” one more time, he just might blow up.</p>
    <p>Yet Steve felt too embarrassed to talk about his deep worries, even with his wife. It seemed like all he could do was pour another glass of wine and suffer in isolation.</p>
  </section>

  <div class="case-tag">“Steven”<br>Brookhaven, PA</div>

  <p class="intro">If you’re like Steve, you’re afraid and alone with plenty of company. In a September 2009 Lakeshore Research Council poll, 80 percent reported the economy is causing significant stress, up from 66 percent from the previous April. The Restful Nights Foundation said 27 percent of people surveyed had sleeplessness because of economic anxiety.</p>

  <section class="body-copy">
    <p class="question">How can you take control of these worries and get back to enjoying your life?</p>
    <p class="list-intro">In this 5 session coaching process you will:</p>
    <ul class="benefits">
      <li>Learn a decision making tool to make choices that truly serve your needs</li>
      <li>Clarify and more fully engage with your purpose and passions</li>
      <li>Improve your relationship with your financial advisor</li>
      <li>Feel more in control and confident in your financial life</li>
    </ul>
    <p>This process guides you to step back and understand the source of your financial worry—your unique story about the meaning of money. Your money story drives your emotions and decision making—for better and worse. You’ll learn a decision making tool for more conscious, effective and satisfying financial and life decisions.</p>
    <p>You’ll also examine your core values and strengths—what really matters most to you and how you work at your best. When you use your money and your core strengths to pursue your highest aspirations, life and wealth become balanced. As you commit more fully to your mission and passions, satisfaction grows and money worries melt away.</p>
  </section>

  <aside class="coach-card">
    <p><strong>Dana Whitlow, Ph.D.</strong> is a psychologist with 30 years of experience treating anxiety and stress. She is co-founder and facilitator of Keystone Circle, a peer learning group for high net worth investors.</p>
    <p><strong>For more information:</strong><br>call 267-555-0188.<br>dwhitlow@keystonecircle.example</p>
  </aside>

  <div class="brand-mark">KEYSTONE<br>CIRCLE</div>

  <section class="offer">
    <p class="offer-title">A Six Week Program to:</p>
    <ul class="offer-list">
      <li>Reduce stress</li>
      <li>Improve performance</li>
      <li>Restore Control</li>
    </ul>
    <p class="offer-contact">Dana Whitlow (215)555-0147</p>
    <div class="price"><span class="amount">$995</span>Money Back Guarantee</div>
  </section>
</main>
</body>
</html>
```